Book Cover

Book Title: THE QUIET LEDGER
Book Sub Title: Notes on slowing the daily rush and shaping a calmer household rhythm
Vibe: Professional, stylish, trustworthy (high-end men's fashion)
Website (for inspiration): www.brindlequarry.com
Attached: a potential photo to use for the cover, but open to other options (from our website)

```html
<!DOCTYPE html>
<html lang="en">
<head>
<meta charset="utf-8">
<title>The Quiet Ledger — Cover Spread</title>
<link rel="stylesheet" href="https://fonts.googleapis.com/css2?family=Bodoni+Moda:wght@600;700;800&family=Oswald:wght@500&display=swap">
<style>
  :root {
    --backdrop: #ecf5f4;
    --navy: #2e3a46;
    --bronze: #7d6847;
    --tan-light: #d4ab86;
    --tan-dark: #b78760;
    --room-light: #e9e3da;
    --room-dark: #b9a58b;
    --ink-light: #ffffff;
    --seam: #f4f6f6;
  }
  * { box-sizing: border-box; margin: 0; padding: 0; }
  html, body {
    width: 706px; height: 1200px; overflow: hidden;
    background: var(--backdrop);
  }
  .canvas { position: relative; width: 706px; height: 1200px; }

  .spread {
    position: absolute; left: 23px; top: 375px;
    width: 1100px; height: 750px;
    transform: scale(0.6); transform-origin: top left;
    background: var(--seam);
    box-shadow: 0 6px 20px rgba(0,0,0,0.25);
  }
  .panel { position: absolute; top: 0; height: 750px; background: var(--navy); overflow: hidden; }
  .back-cover { left: 0; width: 511px; }
  .spine { left: 516px; width: 68px; }
  .front-cover { left: 589px; width: 511px; }

  .tile { position: absolute; width: 42px; height: 42px; background: var(--bronze); }

  .lookbook-grid {
    position: absolute; left: 61px; top: 84px; width: 389px; height: 582px;
    display: grid; grid-template-columns: repeat(3, 1fr); grid-template-rows: repeat(3, 1fr);
  }
  .lookbook-cell {
    background: radial-gradient(ellipse at 50% 40%, var(--tan-light), var(--tan-dark));
    border: 0.5px solid rgba(120,80,50,0.15);
  }

  .spine-title {
    position: absolute; left: 50%; top: 94px;
    transform: translateX(-50%);
    writing-mode: vertical-rl;
    font-family: "Bodoni Moda", serif; font-weight: 600;
    font-size: 38px; letter-spacing: 5px; color: var(--ink-light);
    white-space: nowrap;
  }

  .cover-title {
    position: absolute; left: 0; width: 511px; top: 44px;
    text-align: center; color: var(--ink-light);
    font-family: "Bodoni Moda", serif; font-weight: 800;
    text-shadow: 2px 2px 3px rgba(0,0,0,0.45);
  }
  .cover-title .kicker { display: block; font-size: 34px; letter-spacing: 3px; line-height: 1.1; font-weight: 700; }
  .cover-title .headline { display: block; font-size: 50px; letter-spacing: 5px; line-height: 1.15; }

  .accent-bar { position: absolute; width: 23px; height: 198px; background: var(--bronze); }
  .hero-photo {
    position: absolute; left: 119px; top: 176px; width: 271px; height: 396px;
    background: linear-gradient(180deg, var(--room-light) 0%, #d8cfc2 55%, var(--room-dark) 100%);
  }

  .cover-subtitle {
    position: absolute; left: 0; width: 511px; top: 624px;
    text-align: center; color: var(--ink-light);
    font-family: "Oswald", sans-serif; font-weight: 500;
    font-size: 19px; letter-spacing: 2.6px; line-height: 36px;
    text-transform: uppercase;
    text-shadow: 1px 1px 2px rgba(0,0,0,0.4);
  }
</style>
</head>
<body>
<main class="canvas">
  <section class="spread" aria-label="Book cover spread: The Quiet Ledger">

    <div class="panel back-cover">
      <div class="tile" style="left:428px;top:0"></div>
      <div class="tile" style="left:469px;top:41px"></div>
      <div class="lookbook-grid" role="img" aria-label="Nine-photo lookbook of a man in tailored suits and jackets on a tan studio backdrop">
        <div class="lookbook-cell"></div><div class="lookbook-cell"></div><div class="lookbook-cell"></div>
        <div class="lookbook-cell"></div><div class="lookbook-cell"></div><div class="lookbook-cell"></div>
        <div class="lookbook-cell"></div><div class="lookbook-cell"></div><div class="lookbook-cell"></div>
      </div>
      <div class="tile" style="left:0;top:667px"></div>
      <div class="tile" style="left:41px;top:708px"></div>
    </div>

    <div class="panel spine">
      <span class="spine-title">THE QUIET LEDGER</span>
    </div>

    <div class="panel front-cover">
      <div class="tile" style="left:428px;top:0"></div>
      <div class="tile" style="left:469px;top:41px"></div>

      <h1 class="cover-title">
        <span class="kicker">THE QUIET</span>
        <span class="headline">LEDGER</span>
      </h1>

      <div class="accent-bar" style="left:96px;top:176px"></div>
      <div class="hero-photo" role="img" aria-label="Photo of a man in a navy suit seated on a wooden stool in a bright loft beside a rack of jackets"></div>
      <div class="accent-bar" style="left:390px;top:374px;width:21px"></div>

      <p class="cover-subtitle">Notes on slowing the daily rush and shaping<br>a calmer household rhythm.</p>

      <div class="tile" style="left:0;top:667px"></div>
      <div class="tile" style="left:41px;top:708px"></div>
    </div>

  </section>
</main>
</body>
</html>
```